Vitahaven - Quality health delivered at your door

Vitahaven offers home and Community Based Services for adults who wish to continue live independently in their communities. We increase accessibility to health care, reduce health care delivery gap, reduce mortality and morbidity, reduce health while promoting healthy living in the comfort of our patients communities or homes.

We provide on site services and deliver high quality healthcare at your door. Our experienced physicians coordinate care with our certified nurse practitioners and provide chronic care management, physical therapy, rehabilitation and medications management.

Target Market(s)

Older population living in independent living facilities

Industry/Entity Type

Health Care

Contact Information for Business Card

Vitahaven

Number of Pages Required

4 page

Font styles to use
Sans Serif

Colors

Designer to choose colors to be used in the design.

```html
<!DOCTYPE html>
<html lang="en">
<head>
<meta charset="utf-8">
<title>Vitahaven – Quality health delivered at your door</title>
<link rel="stylesheet" href="https://fonts.googleapis.com/css2?family=Josefin+Sans:wght@300;400;600;700&family=Open+Sans:ital,wght@0,400;0,600;1,400&display=swap">
<style>
:root{
  --green:#7a9a2c;
  --orange:#f0a020;
  --ink:#222;
  --body:#444;
  --muted:#888;
  --band:#eeeeec;
  --footer:#262626;
  --dark-btn:#1d2a0c;
  --hero-light:#f3f3f1;
  --scrubs:#8ccfc6;
  --scrubs-deep:#5fb2a9;
  --skin:#e8c9b0;
  --hair:#b8623a;
  --robe:#ecebe7;
}
*{box-sizing:border-box;margin:0;padding:0}
html,body{width:683px;height:1200px;overflow:hidden}
body{position:relative;background:#fff;font-family:"Open Sans",Arial,sans-serif;color:var(--body)}
.abs{position:absolute}
.top-nav{left:0;top:0;width:683px;height:24px;background:var(--green);display:flex;justify-content:center;gap:16px;align-items:center}
.top-nav a{color:#fff;font-size:6.6px;font-weight:600;text-decoration:none}
.brand{left:64px;top:28px;width:86px;text-align:center}
.brand-mark{display:block;width:40px;height:40px;border-radius:50%;background:var(--orange);border:3px solid var(--green);margin:0 auto 3px}
.brand-name{font-family:"Josefin Sans",Arial,sans-serif;font-size:13px;font-weight:600;color:var(--ink);letter-spacing:.3px}
.social{display:flex;gap:5px}
.social span{width:22px;height:22px;border-radius:50%;background:#7b7b7b;display:block}
.header-social{left:517px;top:27px}
.btn-dark{left:517px;top:60px;width:102px;height:24px;background:var(--dark-btn);color:#fff;font-size:7.3px;font-weight:600;display:flex;align-items:center;justify-content:center;letter-spacing:.2px}
.hero{left:0;top:96px;width:683px;height:294px;background:var(--hero-light)}
.hero-photo{left:250px;top:96px;width:433px;height:294px;
  background:linear-gradient(100deg,var(--hero-light) 0%,#eedfd0 10%,var(--hair) 20%,var(--skin) 28%,var(--scrubs) 38%,var(--scrubs-deep) 48%,var(--scrubs) 55%,var(--robe) 64%,var(--skin) 74%,#c9bdb2 84%,#e9ece9 100%)}
.hero-title{left:65px;top:164px;font-family:"Josefin Sans",Arial,sans-serif;font-size:24.5px;line-height:34.5px;color:var(--ink);font-weight:400}
.btn-green{width:97px;height:25px;background:var(--green);color:#fff;font-size:8.6px;display:flex;align-items:center;justify-content:center;border:1px solid #b8cc80}
.hero-btn{left:64px;top:310px}
.services{left:0;top:390px;width:683px;height:254px;background:var(--band)}
.section-title{width:683px;left:0;text-align:center;font-family:"Josefin Sans",Arial,sans-serif;font-size:21px;font-weight:400;color:var(--ink)}
.section-title em{font-style:normal;color:var(--orange)}
.divider{left:222px;width:240px;height:1px;background:#d6d6d6}
.divider::after{content:"";position:absolute;left:117px;top:-3px;width:6px;height:6px;border-radius:50%;background:var(--green)}
.service{width:126px}
.service-head{display:flex;align-items:center;gap:6px;height:24px}
.service-head h3{font-family:"Josefin Sans",Arial,sans-serif;font-size:9.5px;font-weight:700;color:var(--ink);letter-spacing:.2px;white-space:nowrap}
.service p{font-size:6.5px;line-height:12.6px;color:var(--body);margin-top:8px}
.read-more{font-size:6.5px;color:var(--orange);margin-top:6px;display:block}
.testimonial{width:176px;text-align:center}
.quote-mark{width:22px;height:22px;border-radius:50%;border:1.5px solid var(--orange);margin:0 auto;display:flex;align-items:center;justify-content:center;color:var(--orange);font-size:13px;font-family:Georgia,serif;line-height:1}
.avatar{width:50px;height:50px;border-radius:50%;border:2px solid var(--orange);margin:15px auto 0;background:linear-gradient(#8a6a55,#d8b8a0)}
.testimonial p{font-size:6.5px;line-height:12.6px;color:var(--body);margin-top:17px}
.testimonial .name{color:var(--orange);margin-top:9px;display:block;font-size:6.5px}
.work-card{width:175px}
.work-photo{width:175px;height:96px;box-shadow:0 1px 3px rgba(0,0,0,.3)}
.work-card h4{font-size:7px;font-weight:600;color:#333;margin-top:11px}
.work-card span{font-size:6px;font-style:italic;color:var(--muted);display:block;margin-top:2px}
.footer{left:0;top:1132px;width:683px;height:68px;background:var(--footer)}
.footer-btn{left:64px;top:1153px}
.footer-social{left:294px;top:1157px;gap:9px}
.footer-social span{width:12px;height:12px;background:#ddd}
.rights{left:0;width:683px;top:1176px;text-align:center;color:#ccc;font-size:6px}
.footer-brand{left:555px;top:1138px;width:70px;text-align:center}
.footer-brand .brand-mark{width:34px;height:34px;background:#999;border:2px solid #ccc;margin-bottom:2px}
.footer-brand .brand-name{color:#ddd;font-size:11px}
</style>
</head>
<body>
<nav class="abs top-nav">
  <a>Assisted Living</a><a>Skilled Nursing</a><a>Independent Living</a><a>Home and Community Based Services</a><a>Respite Care</a><a>Rehabilitation</a><a>Brightmind Learning Center</a><a>Contact</a>
</nav>

<div class="abs brand"><span class="brand-mark"></span><span class="brand-name">VITAHAVEN</span></div>
<div class="abs social header-social"><span></span><span></span><span></span><span></span></div>
<div class="abs btn-dark">REQUEST A HOUSECALL</div>

<div class="abs hero"></div>
<div class="abs hero-photo" role="img" aria-label="Photo of a smiling nurse in teal scrubs caring for an elderly woman at home"></div>
<h1 class="abs hero-title">We Provide<br>On Site Services And<br>Deliver High Quality<br>Healthcare At Your Door</h1>
<div class="abs btn-green hero-btn">Request a Housecall</div>

<section class="abs services"></section>
<h2 class="abs section-title" style="top:418px">Our <em>Services</em></h2>
<div class="abs divider" style="top:455px"></div>

<div class="abs service" style="left:65px;top:474px">
  <div class="service-head"><svg width="22" height="20" viewBox="0 0 22 20"><circle cx="7" cy="4" r="3" fill="#f0a020"/><path d="M2 14h18v3H2zM4 11l6-3 6 3" fill="none" stroke="#f0a020" stroke-width="2"/></svg><h3>PHYSICAL THERAPY</h3></div>
  <p>The standard chunk of Lorem Ipsum used since the 1500s is reprodu below for those interested. Sections 1.10.32 and 1.10.33 fro m "de Finibus Bonorum et Malorum" by Cicero are also reproduced in their exact original form, accompanied by English vers ions from the 1914.</p>
  <span class="read-more">Read More »</span>
</div>
<div class="abs service" style="left:208px;top:474px">
  <div class="service-head"><svg width="22" height="20" viewBox="0 0 22 20"><circle cx="11" cy="7" r="5" fill="none" stroke="#f0a020" stroke-width="2"/><path d="M2 12c3 6 15 6 18 0" fill="none" stroke="#f0a020" stroke-width="2"/></svg><h3>MENTAL HEALTH</h3></div>
  <p>The standard chunk of Lorem Ipsum used since the 1500s is reprodu below for those interested. Sections 1.10.32 and 1.10.33 fro m "de Finibus Bonorum et Malorum" by Cicero are also reproduced in their exact original form, accompanied by English vers ions from the 1914.</p>
  <span class="read-more">Read More »</span>
</div>
<div class="abs service" style="left:350px;top:474px">
  <div class="service-head"><svg width="22" height="20" viewBox="0 0 22 20"><path d="M5 2c3 0 4 1 6 1s3-1 6-1c3 2 2 7 0 9l-1 7h-2l-2-6-2 6H8l-1-7C5 9 2 4 5 2z" fill="none" stroke="#f0a020" stroke-width="2"/></svg><h3>DENTAL HEALTH</h3></div>
  <p>The standard chunk of Lorem Ipsum used since the 1500s is reprodu below for those interested. Sections 1.10.32 and 1.10.33 fro m "de Finibus Bonorum et Malorum" by Cicero are also reproduced in their exact original form, accompanied by English vers ions from the 1914.</p>
  <span class="read-more">Read More »</span>
</div>
<div class="abs service" style="left:493px;top:474px">
  <div class="service-head"><svg width="24" height="20" viewBox="0 0 24 20"><path d="M1 4h13v11H1zM14 8h5l4 4v3h-9z" fill="#f0a020"/><circle cx="6" cy="16" r="2.5" fill="#fff" stroke="#f0a020" stroke-width="1.5"/><circle cx="18" cy="16" r="2.5" fill="#fff" stroke="#f0a020" stroke-width="1.5"/><path d="M7 6v6M4 9h6" stroke="#fff" stroke-width="1.6"/></svg><h3>TRANSPORTATION</h3></div>
  <p>The standard chunk of Lorem Ipsum used since the 1500s is reprodu below for those interested. Sections 1.10.32 and 1.10.33 fro m "de Finibus Bonorum et Malorum" by Cicero are also reproduced in their exact original form, accompanied by English vers ions from the 1914.</p>
  <span class="read-more">Read More »</span>
</div>

<h2 class="abs section-title" style="top:666px">Our <em>Customers Says</em></h2>
<div class="abs divider" style="top:703px"></div>

<div class="abs testimonial" style="left:62px;top:732px">
  <div class="quote-mark">“</div>
  <div class="avatar" role="img" aria-label="Portrait of a female customer"></div>
  <p>The standard chunk of Lorem Ipsum used since the 1500s is reproduced below for those interested. Sections 1.10.32 and 1.10.33 from "de Finibus Bonorum et Malorum" by Cicero are also reproduced in their exact original</p>
  <span class="name">Miss Customer Name</span>
</div>
<div class="abs testimonial" style="left:253px;top:732px">
  <div class="quote-mark">“</div>
  <div class="avatar" role="img" aria-label="Portrait of a male customer"></div>
  <p>The standard chunk of Lorem Ipsum used since the 1500s is reproduced below for those interested. Sections 1.10.32 and 1.10.33 from "de Finibus Bonorum et Malorum" by Cicero are also reproduced in their exact original</p>
  <span class="name">Miss Customer Name</span>
</div>
<div class="abs testimonial" style="left:444px;top:732px">
  <div class="quote-mark">“</div>
  <div class="avatar" role="img" aria-label="Portrait of a female customer"></div>
  <p>The standard chunk of Lorem Ipsum used since the 1500s is reproduced below for those interested. Sections 1.10.32 and 1.10.33 from "de Finibus Bonorum et Malorum" by Cicero are also reproduced in their exact original</p>
  <span class="name">Miss Customer Name</span>
</div>

<h2 class="abs section-title" style="top:924px">Our <em>Work</em></h2>
<div class="abs divider" style="top:953px"></div>

<div class="abs work-card" style="left:64px;top:978px">
  <div class="work-photo" role="img" aria-label="Photo of nursing students in blue scrubs during a training session" style="background:linear-gradient(135deg,#d9dfe6,#4d79b8 60%,#2f5a96)"></div>
  <h4>Training for Health care</h4><span>News &amp; Events</span>
</div>
<div class="abs work-card" style="left:253px;top:978px">
  <div class="work-photo" role="img" aria-label="Photo of healthcare staff in a group training meeting" style="background:linear-gradient(135deg,#e8e8e6,#8aa0b8 55%,#3a6f9a)"></div>
  <h4>Training for Health care</h4><span>News &amp; Events</span>
</div>
<div class="abs work-card" style="left:443px;top:978px">
  <div class="work-photo" role="img" aria-label="Photo of a CPR training class with an instructor" style="background:linear-gradient(135deg,#e4e0d8,#c9a88a 50%,#c06a3a)"></div>
  <h4>Training for Health care</h4><span>News &amp; Events</span>
</div>

<footer class="abs footer"></footer>
<div class="abs btn-green footer-btn">Request a Housecall</div>
<div class="abs social footer-social"><span></span><span></span><span></span><span></span><span></span></div>
<div class="abs rights">All Rights Reserved</div>
<div class="abs footer-brand"><span class="brand-mark"></span><span class="brand-name">VITAHAVEN</span></div>
</body>
</html>
```